Coffee roasting needs homepage with web shop

small roasting (no cafe!) needs a simple website with a web shop. We sell coffee to dealers and end customers. The shop should be for end consumers as well as for B2B customers. A login should be available. The design should be modern and at the same time classic with subtle (dark) colors. We need the tabs "Coffee, Shop, Contact, Coffee, Coffee, Login, About Us, Imprint, Privacy" Logo nr 1 should be used from attached file

Target Market(s)

B2B

Number of Pages Required

5+ page

Font styles to use
Sans Serif

Colors

Designer to choose only greyscale colors for use in the design.

Requirements
Must have
• Webshop

```html
<!DOCTYPE html>
<html lang="en">
<head>
<meta charset="utf-8">
<title>Brennhaus – Coffee Roastery</title>
<link rel="stylesheet" href="https://fonts.googleapis.com/css2?family=Open+Sans:wght@400;600;700;800&display=swap">
<style>
  :root{
    --ink:#000;
    --night:#070707;
    --panel:#111;
    --white:#fff;
    --paper:#f4f4f4;
    --muted:#bdbdbd;
    --copper:#c0692e;
    --gold:#d8b45a;
    --gold-pale:#f1d98e;
    --line-gold:#6b5a2a;
  }
  *{margin:0;padding:0;box-sizing:border-box}
  html,body{width:1200px;height:4129px;overflow:hidden;background:var(--ink)}
  body{font-family:"Open Sans",sans-serif;color:var(--white);position:relative}
  .abs{position:absolute}

  /* hero */
  .hero{left:0;top:0;width:1200px;height:726px;
    background:radial-gradient(ellipse at 78% 50%,#3a2c20 0%,#1b1510 35%,#0b0a09 70%,#050505 100%)}
  .hero-photo{left:640px;top:0;width:560px;height:726px;
    background:radial-gradient(circle at 55% 55%,rgba(90,60,38,.55) 0%,rgba(40,28,20,.3) 45%,rgba(0,0,0,0) 75%)}
  .brand-box{left:59px;top:0;width:287px;height:327px;background:var(--paper);
    display:flex;align-items:center;justify-content:center}
  .brand-ring{width:250px;height:250px;border:4px solid #111;border-radius:50%;
    display:flex;align-items:center;justify-content:center}
  .brand-name{font-weight:600;font-size:38px;color:#111}
  .nav a{position:absolute;top:76px;font-size:15px;font-weight:700;letter-spacing:.5px;color:var(--white);text-decoration:none}
  .nav .active::after{content:"";position:absolute;left:0;right:0;top:28px;height:2px;
    background:linear-gradient(90deg,var(--copper) 60%,transparent 60%,transparent 68%,var(--muted) 68%)}
  .login{left:1003px;top:61px;width:131px;height:49px;background:var(--paper);color:#111;
    font-weight:700;font-size:15px;display:flex;align-items:center;justify-content:center}
  .hero-title{left:59px;top:400px;font-size:61px;line-height:77px;font-weight:800;letter-spacing:.5px}
  .hero-sub{left:59px;top:551px;font-size:17px}
  .social{display:flex;gap:18px}
  .social span{width:35px;height:35px;border:2px solid var(--white);border-radius:50%}
  .hero-social{left:59px;top:598px}
  .chevron{left:735px;top:415px}

  /* shared */
  .kicker{font-size:35px;font-weight:700;letter-spacing:7px;
    background:linear-gradient(180deg,#f3e2c4,#8c6a45);-webkit-background-clip:text;background-clip:text;color:transparent}
  .big{font-size:59px;font-weight:700;line-height:66px;letter-spacing:.5px}
  .copy{font-size:13.5px;line-height:16px;text-align:justify}
  .btn{height:52px;border:3px solid var(--white);display:flex;align-items:center;gap:18px;
    padding-left:34px;font-size:19px;font-weight:600;letter-spacing:1px}
  .btn svg{flex:none}

  /* fresh */
  .fresh-photo{left:101px;top:860px;width:381px;height:529px;
    background:linear-gradient(180deg,#5a3a20 0%,#2a2622 35%,#3c3026 65%,#7a4e28 80%,#1a1816 100%);
    box-shadow:-20px 20px 40px rgba(60,60,60,.25)}
  .fresh-text{left:559px;top:938px;width:513px}

  /* shop */
  .shop{left:0;top:1458px;width:1200px;height:761px;
    background:radial-gradient(ellipse at 50% 40%,#1b1b1b,#0b0b0b 70%,#050505)}
  .shop-head{left:0;top:1500px;width:1200px;text-align:center}
  .shop-head small{display:block;font-size:18px;font-weight:600;margin-left:-4px}
  .shop-head h2{font-size:60px;font-weight:700;line-height:70px}
  .shop-head h2::before,.shop-head h2::after{content:"·";margin:0 14px;font-size:40px;vertical-align:middle}
  .card{top:1666px;width:348px;height:484px;display:flex;justify-content:center;
    padding-top:51px;font-size:36px;font-weight:700;line-height:45px;text-align:center}
  .card-enhanced{left:59px;background:linear-gradient(160deg,#5a4630 0%,#2d2218 50%,#1a130d 100%)}
  .card-reserve{left:423px;background:linear-gradient(170deg,#2a2622 0%,#6b4c2c 45%,#3a3a40 75%,#1c1d22 100%)}
  .card-gear{left:787px;width:338px;padding-top:73px;background:linear-gradient(160deg,#26272a 0%,#3b3631 50%,#5a5750 80%,#1a1a1a 100%)}

  /* about */
  .about-text{left:77px;top:2414px;width:514px}
  .about-photo{left:639px;top:2347px;width:561px;height:384px;
    background:radial-gradient(circle at 48% 42%,#c88a45 0%,#9b6a3c 18%,#e4e0da 30%,#8a8580 55%,#3d3f3a 100%);
    box-shadow:20px 20px 40px rgba(60,60,60,.25)}
  .gold-rule{left:0;width:1200px;height:2px;background:linear-gradient(90deg,transparent,var(--line-gold) 40%,var(--line-gold) 70%,transparent)}

  /* contact */
  .contact-photo{left:100px;top:3020px;width:420px;height:540px;
    background:radial-gradient(ellipse at 45% 60%,#5a3a22 0%,#2a1e16 30%,#121212 60%,transparent 80%)}
  .talk{left:609px;top:3010px;display:flex;align-items:flex-start;gap:14px}
  .talk h2{font-size:58px;font-weight:800}
  .talk-copy{left:609px;top:3104px;width:510px;font-size:13px;line-height:16px}
  .dash{left:609px;top:3178px;width:503px;border-top:2px dashed var(--white)}
  .req{left:616px;top:3208px;font-size:11px;color:var(--muted)}
  .req b,.label b{color:var(--copper)}
  .label{font-size:16px;font-weight:700}
  .field{border:3px solid var(--white)}

  /* footer */
  .footer{left:0;top:3694px;width:1200px;height:386px;background:linear-gradient(180deg,#0c0c0c,#050505)}
  .foot-ring{left:499px;top:3745px;width:200px;height:200px;border:4px solid var(--gold);border-radius:50%;
    display:flex;align-items:center;justify-content:center;font-size:30px;font-weight:600;color:var(--gold)}
  .foot-nav{left:0;top:3979px;width:1200px;text-align:center;font-size:14px;color:var(--muted)}
  .foot-nav span{margin:0 10px}
  .foot-social{left:504px;top:4034px}
  .foot-social span{border-color:var(--gold)}
  .copyright{left:0;top:4080px;width:1200px;height:49px;background:var(--gold-pale);color:#222;
    font-size:13px;display:flex;align-items:center;justify-content:center}
</style>
</head>
<body>

<section class="abs hero"></section>
<div class="abs hero-photo" role="img" aria-label="Dark photo of a hand coffee grinder filled with roasted beans"></div>
<div class="abs brand-box"><div class="brand-ring"><span class="brand-name">Brennhaus</span></div></div>
<nav class="nav">
  <a class="active" style="left:513px">COFFEE</a>
  <a style="left:640px">SHOP</a>
  <a style="left:752px">CONTACT</a>
  <a style="left:888px">ABOUT US</a>
</nav>
<div class="abs login">LOGIN</div>
<h1 class="abs hero-title">AMAZING COFFEE<br>THAT TASTE’S RIGHT!</h1>
<p class="abs hero-sub">MAKING IT PERFECT FOR RESTAURANTS, BAKERIES, BARS OR COFFEE SHOPS</p>
<div class="abs social hero-social"><span></span><span></span><span></span><span></span></div>
<svg class="abs chevron" width="85" height="132" viewBox="0 0 85 132"><polyline points="6,4 78,66 6,128" fill="none" stroke="var(--copper)" stroke-width="7"/></svg>

<div class="abs fresh-photo" role="img" aria-label="Photo of a roastery counter with shelves, pendant lamp and coffee grinders"></div>
<div class="abs fresh-text">
  <div class="kicker">FRESH</div>
  <div class="big">ROASTED COFFEE</div>
  <p class="copy" style="margin-top:12px">Lorem ipsum dolor sit amet, consectetur adipiscing elit, sed do eiusmod tempor incididunt ut labore et dolore magna aliqua. Ut enim ad minim veniam, quis nostrud exercitation ullamco laboris nisi ut aliquip ex ea commodo consequat. Duis aute irure dolor in reprehenderit in voluptate velit esse cillum dolore eu fugiat nulla pariatur. Excepteur sint occaecat cupidatat non proident, sunt in culpa qui officia deserunt mollit anim id est laborum</p>
  <div class="btn" style="width:234px;margin-top:28px"><svg width="22" height="18" viewBox="0 0 22 18"><path d="M1 9h19M12 1l8 8-8 8" fill="none" stroke="#fff" stroke-width="2.5"/></svg>SHOP NOW</div>
</div>

<section class="abs shop"></section>
<div class="abs shop-head"><small>OUR SPECIAL MENU</small><h2>SHOP</h2></div>
<div class="abs card card-enhanced" role="img" aria-label="Photo of roasted coffee beans in a tin">ENHANCED<br>COFFEE</div>
<div class="abs card card-reserve" role="img" aria-label="Photo of latte art being poured into a white cup">ROAST<br>RESERVE</div>
<div class="abs card card-gear" role="img" aria-label="Photo of an espresso machine brewing into a cup">GEAR</div>

<div class="abs about-text">
  <div class="kicker">A LITTLE</div>
  <div class="big">ABOUT US</div>
  <p class="copy" style="margin-top:8px">Lorem ipsum dolor sit amet, consectetur adipiscing elit, sed do eiusmod tempor incididunt ut labore et dolore magna aliqua. Ut enim ad minim veniam, quis nostrud exercitation ullamco laboris nisi ut aliquip ex ea commodo consequat. Duis aute irure dolor in reprehenderit in voluptate velit esse cillum dolore eu fugiat nulla pariatur. Excepteur sint occaecat cupidatat non proident, sunt in culpa qui officia deserunt mollit anim id est laborum</p>
  <div class="btn" style="width:234px;margin-top:28px"><svg width="22" height="18" viewBox="0 0 22 18"><path d="M1 9h19M12 1l8 8-8 8" fill="none" stroke="#fff" stroke-width="2.5"/></svg>MAKE ORDER</div>
</div>
<div class="abs about-photo" role="img" aria-label="Photo of a cappuccino with swan latte art on a wooden table with spices"></div>

<div class="abs gold-rule" style="top:2875px"></div>

<div class="abs contact-photo" role="img" aria-label="Photo of a copper French press and a glass of coffee on coffee beans"></div>
<div class="abs talk">
  <h2>LET’S TALK!</h2>
  <svg width="56" height="56" viewBox="0 0 56 56" style="margin-top:-12px"><path d="M20 4c-4 5 4 7 0 12M28 2c-4 5 4 7 0 12" fill="none" stroke="var(--copper)" stroke-width="2"/><path d="M8 24h34v6c0 10-6 16-17 16S8 40 8 30z" fill="none" stroke="var(--copper)" stroke-width="2.5"/><path d="M42 28h5a4 4 0 0 1 0 8h-6" fill="none" stroke="var(--copper)" stroke-width="2.5"/><path d="M4 50h44" stroke="var(--copper)" stroke-width="2.5"/></svg>
</div>
<p class="abs talk-copy">We have great options for wholesale orders to your restaurant, hotel, or business. If you’d like to learn more about carrying our coffee or have any other questions please reach out!</p>
<div class="abs dash"></div>
<div class="abs req"><b>*</b> Indicates required field</div>
<div class="abs label" style="left:614px;top:3250px">NAME: <b>*</b></div>
<div class="abs label" style="left:883px;top:3250px">LAST: <b>*</b></div>
<div class="abs field" style="left:610px;top:3286px;width:254px;height:50px"></div>
<div class="abs field" style="left:880px;top:3286px;width:255px;height:50px"></div>
<div class="abs label" style="left:614px;top:3356px">COMMENT: <b>*</b></div>
<div class="abs field" style="left:610px;top:3385px;width:525px;height:117px"></div>
<div class="abs btn" style="left:610px;top:3529px;width:234px">
  <svg width="22" height="18" viewBox="0 0 22 18"><path d="M1 9h19M12 1l8 8-8 8" fill="none" stroke="#fff" stroke-width="2.5"/></svg>SEND MESSAGE</div>

<footer class="abs footer"></footer>
<div class="abs gold-rule" style="top:3692px"></div>
<div class="abs foot-ring">Brennhaus</div>
<div class="abs foot-nav">
  <span>COFFEE</span>|<span>SHOP</span>|<span>CONTACT</span>|<span>LOGIN</span>|<span>ABOUT US</span>|<span>IMPRINT</span>|<span>PRIVACY</span>
</div>
<div class="abs social foot-social"><span></span><span></span><span></span><span></span></div>
<div class="abs copyright">COPYRIGHT © BRENNHAUS 2019. ALL RIGHT RESERVED</div>

</body>
</html>
```